Dog breeder design card

A card for our dog showing/breeding and companion puppy buyers.
Updates

Reason: The photo's I provided were not seen by designers because of a glitch or error, so I will need to start them over again in the designs submitted to me. I uploaded and emailed the photo's last night.

Thank you all so much for your lovely designs, I like wquite a few of them. I provided images in my original brief, but these apparently did not become available for you to see. I have emailed my images now, so hopefully you may be able to incorporate them into your designs.

Thank you so much for your time,
kind regards,
Beatrice

I have attached the photo’s that can hopefully be incorporated onto my business card. I don’t mind if the whole images aren’t used, but maybe a soft focus look around the adult dog and in a corner of the card maybe....if that’s possible.

Contact Information for Business Card

Corvanel Bullmastiffs, adored by Gerald and Beatrice Lindqvist.
Willowmere NSW
0478 552961

Requirements
Nice to have
• Soft focus look to the outline of adult dogs head incorporated into perhaps a corner of the card. Soft focus outline around pups perhaps.
I do really love hot pink and/or purple text if possible.
"Corvanel Bullmastiffs" to be incorporated on the front of card, our details on reverse.
Would prefer a glossy finish rather than matt.

```html
<!DOCTYPE html>
<html lang="en">
<head>
<meta charset="utf-8">
<title>Corvanel Bullmastiffs – Business Card</title>
<link rel="stylesheet" href="https://fonts.googleapis.com/css2?family=Kaushan+Script&family=Arimo:wght@400&display=swap">
<style>
  :root {
    --backdrop: #e9e5e0;
    --card-white: #ffffff;
    --purple: #7b2a9e;
    --purple-deep: #6a1f8c;
    --glow: #f4e9fa;
    --pink: #e65a9e;
    --pink-soft: #f28cbf;
    --name-purple: #9a3a8f;
    --fawn: #c9a886;
    --fawn-light: #ecdcc6;
  }
  * { margin: 0; padding: 0; box-sizing: border-box; }
  html, body { width: 1200px; height: 900px; overflow: hidden; }
  body { background: var(--backdrop); position: relative; }

  .card {
    position: absolute;
    overflow: hidden;
    box-shadow: 0 2px 6px rgba(0,0,0,0.18);
  }

  /* Front card */
  .card-front {
    left: 123px; top: 115px; width: 510px; height: 315px;
    background: var(--card-white);
  }
  .brand-title {
    position: absolute; left: 0; right: 0; text-align: center;
    font-family: "Kaushan Script", cursive;
    font-weight: 400;
    font-size: 34px; line-height: 1.2;
    letter-spacing: 1.5px; word-spacing: 10px;
    color: var(--pink);
    text-shadow: 1px 1px 1px rgba(120, 40, 90, 0.35);
    white-space: nowrap;
  }
  .card-front .brand-title { top: 16px; }
  .owners {
    position: absolute; left: 32px; top: 112px;
    font-family: "Kaushan Script", cursive;
    font-size: 22px; letter-spacing: 1px;
    color: var(--name-purple);
    white-space: nowrap;
  }
  .contact-line {
    position: absolute; left: 33px;
    font-family: "Arimo", sans-serif;
    font-size: 18px; line-height: 1.2;
    color: var(--pink-soft);
    -webkit-text-stroke: 0.4px var(--name-purple);
    letter-spacing: 0.6px;
    white-space: nowrap;
  }
  .contact-town { top: 152px; }
  .contact-phone { top: 177px; }

  .dog-portrait {
    position: absolute;
    background: radial-gradient(ellipse at 55% 50%, var(--fawn) 0%, var(--fawn-light) 60%, rgba(255,255,255,0) 100%);
  }
  .card-front .dog-portrait { left: 329px; top: 110px; width: 140px; height: 120px; }

  .brand-band {
    position: absolute; left: 0; bottom: 0; width: 100%; height: 68px;
    background:
      radial-gradient(ellipse 42% 70% at 50% 50%, var(--glow) 0%, rgba(244,233,250,0.55) 45%, rgba(123,42,158,0) 100%),
      var(--purple);
  }
  .brand-band .brand-title { top: 10px; }

  /* Back card */
  .card-back {
    left: 567px; top: 477px; width: 508px; height: 313px;
    background:
      radial-gradient(ellipse 48% 42% at 50% 36%, var(--glow) 0%, rgba(244,233,250,0.5) 45%, rgba(123,42,158,0) 100%),
      var(--purple);
  }
  .card-back .brand-title { top: 92px; left: 6px; }
  .card-back .dog-portrait {
    left: 71px; top: 168px; width: 137px; height: 107px;
    background: radial-gradient(ellipse at 55% 50%, var(--fawn) 0%, var(--fawn-light) 70%, var(--purple-deep) 100%);
  }
  .puppy-pair {
    position: absolute; left: 293px; top: 171px; width: 140px; height: 117px;
    background: radial-gradient(ellipse at 50% 50%, var(--fawn-light) 0%, var(--fawn) 55%, rgba(123,42,158,0) 100%);
  }
</style>
</head>
<body>
  <section class="card card-front" aria-label="Business card front">
    <h1 class="brand-title">Corvanel Bullmastiffs</h1>
    <p class="owners">Gerald &amp; Beatrice Lindqvist</p>
    <p class="contact-line contact-town">Willowmere&nbsp; NSW</p>
    <p class="contact-line contact-phone">0478&nbsp; 552961</p>
    <div class="dog-portrait" role="img" aria-label="Photo of an adult fawn bullmastiff head in profile"></div>
    <div class="brand-band">
      <p class="brand-title">Corvanel Bullmastiffs</p>
    </div>
  </section>

  <section class="card card-back" aria-label="Business card back">
    <p class="brand-title">Corvanel Bullmastiffs</p>
    <div class="dog-portrait" role="img" aria-label="Photo of an adult fawn bullmastiff head in profile"></div>
    <div class="puppy-pair" role="img" aria-label="Photo of two fawn bullmastiff puppies lying side by side"></div>
  </section>
</body>
</html>
```